PowerPoint Template - Multiple Slide Backgrounds

Looking for a professional PowerPoint template for a technology company. You will see with the logo there's sort of a theme with gears and a lightbulb of sorts. Keeping with this sort of design could help with the brand.

Branding information
• Logo with transparent background included
• Primary Color (Orange) Hex #E6753D
• Secondary Color (Brown) Hex #6A4238
• Primary Font - Myriad Pro
• Secondary Font - Quiet Sans Light

Design request -
• PowerPoint (POTX) template with master slide views
• Cover Slide
• Color Pallet - 7 Color PowerPoint pallet that includes and complements primary and secondary colors
• Slide Master with Footer
• Multiple Background Types to allow for smart art overlay or bullet point text boxes
Bonus - Sample graphical elements using shapes and smart art

```html
<!DOCTYPE html>
<html lang="en">
<head>
<meta charset="utf-8">
<title>Keystone Ops – Presentation Template Slides</title>
<link href="https://fonts.googleapis.com/css2?family=Roboto:wght@400;500;700&display=swap" rel="stylesheet">
<style>
:root{
  --orange:#e6753d;
  --orange-light:#f3a57e;
  --brown:#6a4238;
  --brown-dark:#5a362d;
  --ink:#3b3b3b;
  --grey-row:#a9a9a9;
  --grey-line:#c9c9c9;
  --backdrop:#c08a57;
}
*{box-sizing:border-box}
html,body{margin:0;padding:0;overflow:hidden}
body{width:896px;height:1200px;background:var(--backdrop);position:relative;font-family:"Roboto",Arial,sans-serif}
.slide{position:absolute;width:406px;height:222px;overflow:hidden;background:linear-gradient(180deg,#fff 0%,#f4f4f4 55%,#dedede 100%);box-shadow:0 3px 7px rgba(0,0,0,.4)}
.col-l{left:37px}.col-r{left:459px}
.head{position:absolute;left:0;top:0}
.title{position:absolute;left:22px;top:4px;margin:0;font:500 20px/24px "Roboto",Arial,sans-serif;color:#fff;white-space:nowrap}
.brand{position:absolute;right:10px;top:13px;display:flex;flex-direction:column;align-items:center}
.brand-dot{width:14px;height:14px;border-radius:50%;background:var(--brown)}
.brand-name{font:700 8.5px/10px "Roboto",Arial,sans-serif;color:var(--orange);margin-top:3px;white-space:nowrap}
.foot{position:absolute;left:0;bottom:0}
.copy{margin:0 0 6px;font:400 6.3px/7.9px "Roboto",Arial,sans-serif;color:var(--ink);text-align:justify}
.cols{position:absolute;top:52px;display:flex;gap:14px}
.cols .col{flex:1}
.sub{margin:0 0 3px;font:700 12px/14px "Roboto",Arial,sans-serif;color:var(--brown)}
.band-text-left{position:absolute;left:20px;top:28px;width:130px}
.band-text-left .cut{float:right;width:130px;height:140px;shape-outside:polygon(130px 0,130px 140px,17px 140px)}
.band-text-right{position:absolute;left:254px;top:112px;width:130px;text-align:right}
.band-text-right .cut{float:left;width:62px;height:74px;shape-outside:polygon(0 0,62px 0,0 74px)}
.band-text-left .copy{text-align:left}
.band-text-right .copy{text-align:right}
.bullets{position:absolute;left:14px;top:60px;width:380px;display:grid;grid-template-columns:repeat(3,1fr);column-gap:8px;row-gap:8px}
.bullet{display:flex;gap:4px;font:400 5.6px/7px "Roboto",Arial,sans-serif;color:var(--ink)}
.bullet b{font-weight:700}
.tick{flex:0 0 7px;height:7px;margin-top:1px}
.gear-text{position:absolute;left:193px;top:55px;width:200px}
.gear-text .copy{font-size:7.4px;line-height:9.4px}
.table{position:absolute;left:30px;top:60px;width:346px;border-top:2px solid var(--grey-line)}
.row{display:flex;align-items:center;height:25px;border-bottom:2px solid #e2e2e2;font:400 6px/7px "Roboto",Arial,sans-serif;color:var(--ink)}
.row.alt{background:var(--grey-row);color:#fff}
.row .month{width:92px;padding-left:14px;font-weight:700;color:#a0523a;font-size:6.5px}
.row.alt .month{color:#fff}
.row .plan{width:56px}
.row .desc{flex:1}
.row .desc b{font-weight:700}
.rings{position:absolute;left:20px;top:58px;width:374px;display:flex;justify-content:space-between}
.ring{width:84px;text-align:center}
.ring h3{margin:2px 0 2px;font:700 10px/12px "Roboto",Arial,sans-serif;color:var(--orange)}
.ring p{margin:0;font:400 5.5px/6.8px "Roboto",Arial,sans-serif;color:var(--ink)}
.chart-note{position:absolute;top:158px;width:180px;text-align:center;font:400 5.6px/7px "Roboto",Arial,sans-serif;color:var(--ink);margin:0}
.headline-text{position:absolute;left:18px;top:44px;width:168px}
.headline-text .copy{font-size:5.6px;line-height:7px;margin-bottom:10px;text-align:left}
</style>
</head>
<body>

<!-- Slide: Two Column Text -->
<section class="slide col-l" style="top:15px">
  <svg class="head" width="406" height="34" viewBox="0 0 406 34"><polygon points="0,0 320,0 296,30 0,30" fill="var(--brown)"/><polygon points="324,0 342,0 318,30 300,30" fill="var(--orange)"/><polygon points="346,0 362,0 344,22 328,22" fill="var(--orange-light)"/><rect x="340" y="0" width="66" height="3" fill="var(--orange-light)"/></svg>
  <h2 class="title">Two Column Text</h2>
  <div class="brand"><span class="brand-dot"></span><span class="brand-name">Keystone Ops</span></div>
  <div class="cols" style="left:28px;width:350px;gap:16px">
    <div class="col">
      <p class="copy">Lorem Ipsum is simply dummy text of the printing and typesetting industry. Lorem Ipsum has been the industry's standard dummy text ever since the 1500s, when an unknown printer took a galley of type and scrambled it to make a type specimen book.</p>
      <p class="copy">Contrary to popular belief, Lorem Ipsum is not simply random text. It has roots in a piece of classical Latin literature from 45 BC, making it over 2000 years old. Daniel Wren, a Latin professor at Harrow Field College in Virginia, looked up one of the more obscure Latin words, consectetur, from a Lorem Ipsum Source.</p>
      <p class="copy">Lorem Ipsum comes from sections 1.10.32 and 1.10.33 of "de Finibus Bonorum et Malorum" (The Extremes of Good and Evil) by Tullius Aven, written in 45 BC. This book is a treatise on the theory of ethics, very popular during the Renaissance.</p>
    </div>
    <div class="col">
      <p class="copy">Lorem Ipsum is simply dummy text of the printing and typesetting industry. Lorem Ipsum has been the industry's standard dummy text ever since the 1500s, when an unknown printer took a galley of type and scrambled it to make a type specimen book.</p>
      <p class="copy">Contrary to popular belief, Lorem Ipsum is not simply random text. It has roots in a piece of classical Latin literature from 45 BC, making it over 2000 years old. Daniel Wren, a Latin professor at Harrow Field College in Virginia, looked up one of the more obscure Latin words, consectetur, from a Lorem Ipsum Source.</p>
      <p class="copy">Lorem Ipsum comes from sections 1.10.32 and 1.10.33 of "de Finibus Bonorum et Malorum" (The Extremes of Good and Evil) by Tullius Aven, written in 45 BC. This book is a treatise on the theory of ethics, very popular during the Renaissance.</p>
    </div>
  </div>
  <svg class="foot" width="406" height="10" viewBox="0 0 406 10"><rect x="0" y="5" width="38" height="5" fill="var(--brown)"/><text x="44" y="9" font-family="Roboto, Arial, sans-serif" font-size="7" fill="#333">1</text><polygon points="58,10 62,5 406,5 406,10" fill="var(--orange)"/></svg>
</section>

<!-- Slide: Three Column Text -->
<section class="slide col-r" style="top:15px">
  <svg class="head" width="406" height="34" viewBox="0 0 406 34"><polygon points="0,0 320,0 296,30 0,30" fill="var(--brown)"/><polygon points="324,0 342,0 318,30 300,30" fill="var(--orange)"/><polygon points="346,0 362,0 344,22 328,22" fill="var(--orange-light)"/><rect x="340" y="0" width="66" height="3" fill="var(--orange-light)"/></svg>
  <h2 class="title">Three Column Text</h2>
  <div class="brand"><span class="brand-dot"></span><span class="brand-name">Keystone Ops</span></div>
  <div class="cols" style="left:26px;width:358px;gap:14px">
    <div class="col">
      <p class="copy">Lorem Ipsum is simply dummy text of the printing and typesetting industry. Lorem Ipsum has been the industry's standard dummy text ever since the 1500s, when an unknown printer took a galley of type and scrambled it to make a type specimen book.</p>
      <p class="copy">Contrary to popular belief, Lorem Ipsum is not simply random text. It has roots in a piece of classical Latin literature from 45 BC, making it over 2000 years old. Daniel Wren, a Latin professor at Harrow Field College .</p>
      <p class="copy">Lorem Ipsum comes from sections 1.10.32 and 1.10.33 of "de Finibus Bonorum et Malorum".</p>
    </div>
    <div class="col">
      <p class="copy">Lorem Ipsum is simply dummy text of the printing and typesetting industry. Lorem Ipsum has been the industry's standard dummy text ever since the 1500s, when an unknown printer took a galley of type and scrambled it to make a type specimen book.</p>
      <p class="copy">Contrary to popular belief, Lorem Ipsum is not simply random text. It has roots in a piece of classical Latin literature from 45 BC, making it over 2000 years old. Daniel Wren, a Latin professor at Harrow Field College .</p>
      <p class="copy">Duis aute irure dolor in reprehenderit in voluptate velit esse cillum dolore eu fugiat nulla pariatur.</p>
    </div>
    <div class="col">
      <p class="copy">Lorem Ipsum is simply dummy text of the printing and typesetting industry. Lorem Ipsum has been the industry's standard dummy text ever since the 1500s, when an unknown printer took a galley of type and scrambled it to make a type specimen book.</p>
      <p class="copy">Contrary to popular belief, Lorem Ipsum is not simply random text. It has roots in a piece of classical Latin literature from 45 BC, making it over 2000 years old. Daniel Wren, a Latin professor at Harrow Field College .</p>
    </div>
  </div>
  <svg class="foot" width="406" height="10" viewBox="0 0 406 10"><rect x="0" y="5" width="38" height="5" fill="var(--brown)"/><text x="44" y="9" font-family="Roboto, Arial, sans-serif" font-size="7" fill="#333">1</text><polygon points="58,10 62,5 406,5 406,10" fill="var(--orange)"/></svg>
</section>

<!-- Slide: Diagonal image band -->
<section class="slide col-l" style="top:245px;height:225px">
  <svg width="406" height="225" viewBox="0 0 406 225" style="position:absolute;left:0;top:0" role="img" aria-label="Photo of glowing blue circuit-board lines on a dark blue background">
    <defs><linearGradient id="circuit" x1="0" y1="1" x2="1" y2="0"><stop offset="0" stop-color="#071a5c"/><stop offset=".5" stop-color="#0d3fb0"/><stop offset="1" stop-color="#0a2a86"/></linearGradient></defs>
    <polygon points="180,0 403,0 213,225 0,225 0,220" fill="url(#circuit)"/>
  </svg>
  <div class="band-text-left">
    <div class="cut"></div>
    <h3 class="sub">Lorem Ipsum</h3>
    <p class="copy">Lorem Ipsum is simply dummy text of the printing and typesetting industry. Lorem Ipsum has been the industry's standard dummy text ever since the 1500s, when an unknown printer took a galley of type and scrambled it to make a type specimen book.</p>
    <p class="copy">Contrary to popular belief, Lorem Ipsum is not simply random text.</p>
  </div>
  <div class="band-text-right">
    <div class="cut"></div>
    <h3 class="sub">Lorem Ipsum</h3>
    <p class="copy">Lorem Ipsum is simply dummy text of the printing and typesetting industry. Lorem Ipsum has been the industry's standard dummy text ever since the 1500s, when an unknown printer took a galley of type and scrambled it to make a type specimen book.</p>
    <p class="copy">Contrary to popular belief, Lorem Ipsum is not simply random text.</p>
  </div>
</section>

<!-- Slide: Bullet Text -->
<section class="slide col-r" style="top:245px;height:225px">
  <svg class="head" width="406" height="34" viewBox="0 0 406 34"><polygon points="0,0 320,0 296,30 0,30" fill="var(--brown)"/><polygon points="324,0 342,0 318,30 300,30" fill="var(--orange)"/><polygon points="346,0 362,0 344,22 328,22" fill="var(--orange-light)"/><rect x="340" y="0" width="66" height="3" fill="var(--orange-light)"/></svg>
  <h2 class="title">Bullet Text</h2>
  <div class="brand"><span class="brand-dot"></span><span class="brand-name">Keystone Ops</span></div>
  <div class="bullets">
    <div class="bullet"><svg class="tick" viewBox="0 0 7 7"><rect x=".5" y=".5" width="6" height="6" fill="none" stroke="var(--orange)"/><path d="M1.5 3.5l1.5 1.5 3-4" fill="none" stroke="var(--orange)" stroke-width="1.2"/></svg><span><b>Lorem Ipsum</b> is simply dummy text of the printing and typesetting industry. Lorem Ipsum has been the industry's standard dummy text ever since.</span></div>
    <div class="bullet"><svg class="tick" viewBox="0 0 7 7"><rect x=".5" y=".5" width="6" height="6" fill="none" stroke="var(--orange)"/><path d="M1.5 3.5l1.5 1.5 3-4" fill="none" stroke="var(--orange)" stroke-width="1.2"/></svg><span><b>Lorem Ipsum</b> is simply dummy text of the printing and typesetting industry. Lorem Ipsum has been the industry's standard dummy text ever since.</span></div>
    <div class="bullet"><svg class="tick" viewBox="0 0 7 7"><rect x=".5" y=".5" width="6" height="6" fill="none" stroke="var(--orange)"/><path d="M1.5 3.5l1.5 1.5 3-4" fill="none" stroke="var(--orange)" stroke-width="1.2"/></svg><span><b>Lorem Ipsum</b> is simply dummy text of the printing and typesetting industry. Lorem Ipsum has been the industry's standard dummy text ever since.</span></div>
    <div class="bullet"><svg class="tick" viewBox="0 0 7 7"><rect x=".5" y=".5" width="6" height="6" fill="none" stroke="var(--orange)"/><path d="M1.5 3.5l1.5 1.5 3-4" fill="none" stroke="var(--orange)" stroke-width="1.2"/></svg><span><b>Lorem Ipsum</b> is simply dummy text of the printing and typesetting industry. Lorem Ipsum has been the industry's standard dummy text ever since.</span></div>
    <div class="bullet"><svg class="tick" viewBox="0 0 7 7"><rect x=".5" y=".5" width="6" height="6" fill="none" stroke="var(--orange)"/><path d="M1.5 3.5l1.5 1.5 3-4" fill="none" stroke="var(--orange)" stroke-width="1.2"/></svg><span><b>Lorem Ipsum</b> is simply dummy text of the printing and typesetting industry. Lorem Ipsum has been the industry's standard dummy text ever since.</span></div>
    <div class="bullet"><svg class="tick" viewBox="0 0 7 7"><rect x=".5" y=".5" width="6" height="6" fill="none" stroke="var(--orange)"/><path d="M1.5 3.5l1.5 1.5 3-4" fill="none" stroke="var(--orange)" stroke-width="1.2"/></svg><span><b>Lorem Ipsum</b> is simply dummy text of the printing and typesetting industry. Lorem Ipsum has been the industry's standard dummy text ever since.</span></div>
    <div class="bullet"><svg class="tick" viewBox="0 0 7 7"><rect x=".5" y=".5" width="6" height="6" fill="none" stroke="var(--orange)"/><path d="M1.5 3.5l1.5 1.5 3-4" fill="none" stroke="var(--orange)" stroke-width="1.2"/></svg><span><b>Lorem Ipsum</b> is simply dummy text of the printing and typesetting industry. Lorem Ipsum has been the industry's standard dummy text ever since.</span></div>
    <div class="bullet"><svg class="tick" viewBox="0 0 7 7"><rect x=".5" y=".5" width="6" height="6" fill="none" stroke="var(--orange)"/><path d="M1.5 3.5l1.5 1.5 3-4" fill="none" stroke="var(--orange)" stroke-width="1.2"/></svg><span><b>Lorem Ipsum</b> is simply dummy text of the printing and typesetting industry. Lorem Ipsum has been the industry's standard dummy text ever since.</span></div>
    <div class="bullet"><svg class="tick" viewBox="0 0 7 7"><rect x=".5" y=".5" width="6" height="6" fill="none" stroke="var(--orange)"/><path d="M1.5 3.5l1.5 1.5 3-4" fill="none" stroke="var(--orange)" stroke-width="1.2"/></svg><span><b>Lorem Ipsum</b> is simply dummy text of the printing and typesetting industry. Lorem Ipsum has been the industry's standard dummy text ever since.</span></div>
    <div class="bullet"><svg class="tick" viewBox="0 0 7 7"><rect x=".5" y=".5" width="6" height="6" fill="none" stroke="var(--orange)"/><path d="M1.5 3.5l1.5 1.5 3-4" fill="none" stroke="var(--orange)" stroke-width="1.2"/></svg><span><b>Lorem Ipsum</b> is simply dummy text of the printing and typesetting industry. Lorem Ipsum has been the industry's standard dummy text ever since.</span></div>
    <div class="bullet"><svg class="tick" viewBox="0 0 7 7"><rect x=".5" y=".5" width="6" height="6" fill="none" stroke="var(--orange)"/><path d="M1.5 3.5l1.5 1.5 3-4" fill="none" stroke="var(--orange)" stroke-width="1.2"/></svg><span><b>Lorem Ipsum</b> is simply dummy text of the printing and typesetting industry. Lorem Ipsum has been the industry's standard dummy text ever since.</span></div>
    <div class="bullet"><svg class="tick" viewBox="0 0 7 7"><rect x=".5" y=".5" width="6" height="6" fill="none" stroke="var(--orange)"/><path d="M1.5 3.5l1.5 1.5 3-4" fill="none" stroke="var(--orange)" stroke-width="1.2"/></svg><span><b>Lorem Ipsum</b> is simply dummy text of the printing and typesetting industry. Lorem Ipsum has been the industry's standard dummy text ever since.</span></div>
  </div>
  <svg class="foot" width="406" height="10" viewBox="0 0 406 10"><rect x="0" y="5" width="38" height="5" fill="var(--brown)"/><text x="44" y="9" font-family="Roboto, Arial, sans-serif" font-size="7" fill="#333">1</text><polygon points="58,10 62,5 406,5 406,10" fill="var(--orange)"/></svg>
</section>

<!-- Slide: Percentage Infographic -->
<section class="slide col-l" style="top:478px;height:227px">
  <svg class="head" width="406" height="34" viewBox="0 0 406 34"><polygon points="0,0 320,0 296,30 0,30" fill="var(--brown)"/><polygon points="324,0 342,0 318,30 300,30" fill="var(--orange)"/><polygon points="346,0 362,0 344,22 328,22" fill="var(--orange-light)"/><rect x="340" y="0" width="66" height="3" fill="var(--orange-light)"/></svg>
  <h2 class="title">Gear Infographic</h2>
  <div class="brand"><span class="brand-dot"></span><span class="brand-name">Keystone Ops</span></div>
  <svg width="180" height="170" viewBox="0 0 180 170" style="position:absolute;left:20px;top:45px" font-family="Roboto, Arial, sans-serif" font-weight="700" text-anchor="middle">
    <circle cx="46" cy="55" r="30" fill="#fff" stroke="var(--brown)" stroke-width="13"/>
    <text x="46" y="60" font-size="13" fill="#222">83%</text>
    <circle cx="106" cy="30" r="19" fill="#fff" stroke="var(--orange)" stroke-width="9"/>
    <text x="106" y="34" font-size="11" fill="#222">43%</text>
    <circle cx="114" cy="98" r="34" fill="#fff" stroke="var(--orange)" stroke-width="14"/>
    <text x="114" y="103" font-size="13" fill="#222">66%</text>
    <circle cx="45" cy="127" r="20" fill="#fff" stroke="var(--brown)" stroke-width="10"/>
    <text x="45" y="131" font-size="11" fill="#222">45%</text>
  </svg>
  <div class="gear-text">
    <p class="copy">Lorem Ipsum is simply dummy text of the printing and typesetting industry. Lorem Ipsum has been the industry's standard dummy text ever since the 1500s, when an unknown printer took a galley of type and scrambled it to make a type specimen book.</p>
    <p class="copy">Contrary to popular belief, Lorem Ipsum is not simply random text. It has roots in a piece of classical Latin literature from 45 BC, making it over 2000 years old. Daniel Wren, a Latin professor at Harrow Field College .</p>
    <p class="copy">Lorem Ipsum comes from sections 1.10.32 and 1.10.33 of "de Finibus Bonorum et Malorum".</p>
  </div>
  <svg class="foot" width="406" height="10" viewBox="0 0 406 10"><rect x="0" y="5" width="38" height="5" fill="var(--brown)"/><text x="44" y="9" font-family="Roboto, Arial, sans-serif" font-size="7" fill="#333">1</text><polygon points="58,10 62,5 406,5 406,10" fill="var(--orange)"/></svg>
</section>

<!-- Slide: Headlines with photo -->
<section class="slide col-r" style="top:478px;height:227px">
  <svg width="406" height="227" viewBox="0 0 406 227" style="position:absolute;left:0;top:0" role="img" aria-label="Photo of hands typing on a laptop with a glowing world network of people icons">
    <defs><linearGradient id="laptop" x1="0" y1="0" x2="1" y2="1"><stop offset="0" stop-color="#9fb3c6"/><stop offset=".55" stop-color="#d9dee3"/><stop offset="1" stop-color="#6f6a6b"/></linearGradient></defs>
    <polygon points="200,0 406,0 406,227 120,227" fill="url(#laptop)"/>
  </svg>
  <svg class="head" width="406" height="34" viewBox="0 0 406 34"><polygon points="0,0 210,0 190,30 0,30" fill="var(--brown)"/></svg>
  <h2 class="title" style="font-size:17px;left:18px;top:6px">Headlines Goes Here</h2>
  <div class="headline-text">
    <p class="copy">Lorem ipsum dolor sit amet, consectetur adipiscing elit, sed do eiusmod tempor incididunt ut labore et dolore magna aliqua. Ut enim ad minim veniam, quis nostrud exercitation ullamco laboris nisi ut aliquip ex ea commodo consequat.</p>
    <p class="copy">Lorem ipsum dolor sit amet, consectetur adipiscing elit, sed do eiusmod tempor incididunt ut labore et dolore magna aliqua. Ut enim ad minim veniam, quis nostrud exercitation ullamco laboris nisi ut aliquip ex ea commodo consequat.</p>
    <p class="copy">Lorem ipsum dolor sit amet, consectetur adipiscing elit, sed do eiusmod tempor incididunt ut labore et dolore magna aliqua. Ut enim ad minim veniam, quis nostrud exercitation ullamco laboris nisi ut aliquip ex ea commodo consequat.</p>
  </div>
</section>

<!-- Slide: Table -->
<section class="slide col-l" style="top:715px;height:228px">
  <svg class="head" width="406" height="34" viewBox="0 0 406 34"><polygon points="0,0 320,0 296,30 0,30" fill="var(--brown)"/><polygon points="324,0 342,0 318,30 300,30" fill="var(--orange)"/><polygon points="346,0 362,0 344,22 328,22" fill="var(--orange-light)"/><rect x="340" y="0" width="66" height="3" fill="var(--orange-light)"/></svg>
  <h2 class="title">Headline Goes Here</h2>
  <div class="brand"><span class="brand-dot"></span><span class="brand-name">Keystone Ops</span></div>
  <div class="table">
    <div class="row"><span class="month">August</span><span class="plan">Plan1</span><span class="desc"><b>Lorem Ipsum</b> is simply dummy text of the printing and typesetting industry. Lorem Ipsum has been the industry's standard dummy text</span></div>
    <div class="row alt"><span class="month">September</span><span class="plan">Plan2</span><span class="desc"><b>Lorem Ipsum</b> is simply dummy text of the printing and typesetting industry. Lorem Ipsum has been the industry's standard dummy text</span></div>
    <div class="row"><span class="month">October</span><span class="plan">Plan3</span><span class="desc"><b>Lorem Ipsum</b> is simply dummy text of the printing and typesetting industry. Lorem Ipsum has been the industry's standard dummy text</span></div>
    <div class="row alt"><span class="month">November</span><span class="plan">Plan4</span><span class="desc"><b>Lorem Ipsum</b> is simply dummy text of the printing and typesetting industry. Lorem Ipsum has been the industry's standard dummy text</span></div>
    <div class="row"><span class="month">December</span><span class="plan">Plan4</span><span class="desc"><b>Lorem Ipsum</b> is simply dummy text of the printing and typesetting industry. Lorem Ipsum has been the industry's standard dummy text</span></div>
  </div>
  <svg class="foot" width="406" height="10" viewBox="0 0 406 10"><rect x="0" y="5" width="38" height="5" fill="var(--brown)"/><text x="44" y="9" font-family="Roboto, Arial, sans-serif" font-size="7" fill="#333">1</text><polygon points="58,10 62,5 406,5 406,10" fill="var(--orange)"/></svg>
</section>

<!-- Slide: Circle Chart -->
<section class="slide col-r" style="top:715px;height:228px">
  <svg class="head" width="406" height="34" viewBox="0 0 406 34"><polygon points="0,0 320,0 296,30 0,30" fill="var(--brown)"/><polygon points="324,0 342,0 318,30 300,30" fill="var(--orange)"/><polygon points="346,0 362,0 344,22 328,22" fill="var(--orange-light)"/><rect x="340" y="0" width="66" height="3" fill="var(--orange-light)"/></svg>
  <h2 class="title">Circle Chart</h2>
  <div class="brand"><span class="brand-dot"></span><span class="brand-name">Keystone Ops</span></div>
  <div class="rings">
    <div class="ring">
      <svg width="76" height="76" viewBox="0 0 76 76" font-family="Roboto, Arial, sans-serif"><circle cx="38" cy="38" r="32" fill="#fff" stroke="var(--brown)" stroke-width="9"/><circle cx="38" cy="38" r="32" fill="none" stroke="var(--orange)" stroke-width="9" stroke-dasharray="68.4 201" transform="rotate(-90 38 38)"/><text x="38" y="45" text-anchor="middle" font-size="19" font-weight="500" fill="#222">34%</text></svg>
      <h3>Lorem Ipsum</h3><p>Lorem Ipsum is simply dummy text of the printing and typesetting industry. Lorem Ipsum has been the industry's standard dummy text ever since.</p>
    </div>
    <div class="ring">
      <svg width="76" height="76" viewBox="0 0 76 76" font-family="Roboto, Arial, sans-serif"><circle cx="38" cy="38" r="32" fill="#fff" stroke="var(--brown)" stroke-width="9"/><circle cx="38" cy="38" r="32" fill="none" stroke="var(--orange)" stroke-width="9" stroke-dasharray="110.6 201" transform="rotate(-90 38 38)"/><text x="38" y="45" text-anchor="middle" font-size="19" font-weight="500" fill="#222">55%</text></svg>
      <h3>Lorem Ipsum</h3><p>Lorem Ipsum is simply dummy text of the printing and typesetting industry. Lorem Ipsum has been the industry's standard dummy text ever since.</p>
    </div>
    <div class="ring">
      <svg width="76" height="76" viewBox="0 0 76 76" font-family="Roboto, Arial, sans-serif"><circle cx="38" cy="38" r="32" fill="#fff" stroke="var(--brown)" stroke-width="9"/><circle cx="38" cy="38" r="32" fill="none" stroke="var(--orange)" stroke-width="9" stroke-dasharray="150.8 201" transform="rotate(-90 38 38)"/><text x="38" y="45" text-anchor="middle" font-size="19" font-weight="500" fill="#222">75%</text></svg>
      <h3>Lorem Ipsum</h3><p>Lorem Ipsum is simply dummy text of the printing and typesetting industry. Lorem Ipsum has been the industry's standard dummy text ever since.</p>
    </div>
    <div class="ring">
      <svg width="76" height="76" viewBox="0 0 76 76" font-family="Roboto, Arial, sans-serif"><circle cx="38" cy="38" r="32" fill="#fff" stroke="var(--brown)" stroke-width="9"/><circle cx="38" cy="38" r="32" fill="none" stroke="var(--orange)" stroke-width="9" stroke-dasharray="168.9 201" transform="rotate(-90 38 38)"/><text x="38" y="45" text-anchor="middle" font-size="19" font-weight="500" fill="#222">84%</text></svg>
      <h3>Lorem Ipsum</h3><p>Lorem Ipsum is simply dummy text of the printing and typesetting industry. Lorem Ipsum has been the industry's standard dummy text ever since.</p>
    </div>
  </div>
  <svg class="foot" width="406" height="10" viewBox="0 0 406 10"><rect x="0" y="5" width="38" height="5" fill="var(--brown)"/><text x="44" y="9" font-family="Roboto, Arial, sans-serif" font-size="7" fill="#333">1</text><polygon points="58,10 62,5 406,5 406,10" fill="var(--orange)"/></svg>
</section>

<!-- Slide: Bar Chart -->
<section class="slide col-l" style="top:955px;height:230px">
  <svg class="head" width="406" height="34" viewBox="0 0 406 34"><polygon points="0,0 320,0 296,30 0,30" fill="var(--brown)"/><polygon points="324,0 342,0 318,30 300,30" fill="var(--orange)"/><polygon points="346,0 362,0 344,22 328,22" fill="var(--orange-light)"/><rect x="340" y="0" width="66" height="3" fill="var(--orange-light)"/></svg>
  <h2 class="title">Bar Chart</h2>
  <div class="brand"><span class="brand-dot"></span><span class="brand-name">Keystone Ops</span></div>
  <svg width="400" height="160" viewBox="0 0 400 160" style="position:absolute;left:12px;top:58px" font-family="Roboto, Arial, sans-serif">
    <g stroke="#d4d4d4" stroke-width=".6">
      <line x1="20" y1="5" x2="310" y2="5"/><line x1="20" y1="17" x2="310" y2="17"/><line x1="20" y1="29" x2="310" y2="29"/><line x1="20" y1="41" x2="310" y2="41"/><line x1="20" y1="53" x2="310" y2="53"/><line x1="20" y1="65" x2="310" y2="65"/><line x1="20" y1="77" x2="310" y2="77"/><line x1="20" y1="89" x2="310" y2="89"/><line x1="20" y1="101" x2="310" y2="101"/><line x1="20" y1="113" x2="310" y2="113"/>
    </g>
    <line x1="20" y1="125" x2="310" y2="125" stroke="#888" stroke-width=".8"/>
    <g font-size="5.5" fill="#444" text-anchor="end">
      <text x="16" y="7">50</text><text x="16" y="19">45</text><text x="16" y="31">40</text><text x="16" y="43">35</text><text x="16" y="55">30</text><text x="16" y="67">25</text><text x="16" y="79">20</text><text x="16" y="91">15</text><text x="16" y="103">10</text><text x="16" y="115">5</text><text x="16" y="127">0</text>
    </g>
    <g fill="var(--brown)"><rect x="28" y="21.8" width="10" height="103.2"/><rect x="74.7" y="65" width="10" height="60"/><rect x="121.3" y="41" width="10" height="84"/><rect x="168" y="53" width="10" height="72"/><rect x="214.7" y="17" width="10" height="108"/><rect x="261.3" y="50.6" width="10" height="74.4"/></g>
    <g fill="var(--orange)"><rect x="38" y="69.8" width="10" height="55.2"/><rect x="84.7" y="19.4" width="10" height="105.6"/><rect x="131.3" y="84.2" width="10" height="40.8"/><rect x="178" y="65" width="10" height="60"/><rect x="224.7" y="43.4" width="10" height="81.6"/><rect x="271.3" y="43.4" width="10" height="81.6"/></g>
    <g fill="#4a4a4a"><rect x="48" y="77" width="10" height="48"/><rect x="94.7" y="77" width="10" height="48"/><rect x="141.3" y="53" width="10" height="72"/><rect x="188" y="29" width="10" height="96"/><rect x="234.7" y="57.8" width="10" height="67.2"/><rect x="281.3" y="26.6" width="10" height="98.4"/></g>
    <g font-size="8.5" fill="#222" text-anchor="middle">
      <text x="43" y="139">Category 1</text><text x="89.7" y="139">Category 2</text><text x="136.3" y="139">Category 3</text><text x="183" y="139">Category 4</text><text x="229.7" y="139">Category 4</text><text x="276.3" y="139">Category 5</text>
    </g>
    <g font-size="5.5" fill="#444">
      <rect x="322" y="40" width="9" height="9" fill="var(--brown)"/><text x="336" y="47">Series 1</text>
      <rect x="322" y="56" width="9" height="9" fill="var(--orange)"/><text x="336" y="63">Series 2</text>
      <rect x="322" y="72" width="9" height="9" fill="#4a4a4a"/><text x="336" y="79">Series 3</text>
    </g>
  </svg>
  <svg class="foot" width="406" height="10" viewBox="0 0 406 10"><rect x="0" y="5" width="38" height="5" fill="var(--brown)"/><text x="44" y="9" font-family="Roboto, Arial, sans-serif" font-size="7" fill="#333">1</text><polygon points="58,10 62,5 406,5 406,10" fill="var(--orange)"/></svg>
</section>

<!-- Slide: Line Chart -->
<section class="slide col-r" style="top:955px;height:230px">
  <svg class="head" width="406" height="34" viewBox="0 0 406 34"><polygon points="0,0 320,0 296,30 0,30" fill="var(--brown)"/><polygon points="324,0 342,0 318,30 300,30" fill="var(--orange)"/><polygon points="346,0 362,0 344,22 328,22" fill="var(--orange-light)"/><rect x="340" y="0" width="66" height="3" fill="var(--orange-light)"/></svg>
  <h2 class="title">Line Chart</h2>
  <div class="brand"><span class="brand-dot"></span><span class="brand-name">Keystone Ops</span></div>
  <svg width="200" height="80" viewBox="0 0 200 80" style="position:absolute;left:14px;top:70px" font-family="Roboto, Arial, sans-serif">
    <g stroke="#bbb" stroke-width=".6" stroke-dasharray="2 2">
      <line x1="24" y1="8" x2="185" y2="8"/><line x1="24" y1="16" x2="185" y2="16"/><line x1="24" y1="24" x2="185" y2="24"/><line x1="24" y1="32" x2="185" y2="32"/><line x1="24" y1="40" x2="185" y2="40"/><line x1="24" y1="48" x2="185" y2="48"/><line x1="24" y1="56" x2="185" y2="56"/><line x1="24" y1="64" x2="185" y2="64"/><line x1="24" y1="72" x2="185" y2="72"/>
    </g>
    <text x="18" y="10" font-size="6" text-anchor="end" fill="#333">100%</text>
    <text x="18" y="80" font-size="6" text-anchor="end" fill="#333">0%</text>
    <polyline points="26,58 60,25 80,46 102,30 128,45 148,30 166,38 182,8" fill="none" stroke="var(--brown)" stroke-width="1.2"/>
    <g fill="#fff" stroke="var(--brown)" stroke-width="1"><circle cx="26" cy="58" r="3"/><circle cx="60" cy="25" r="3"/><circle cx="80" cy="46" r="3"/><circle cx="102" cy="30" r="3"/><circle cx="128" cy="45" r="3"/><circle cx="148" cy="30" r="3"/><circle cx="166" cy="38" r="3"/><circle cx="182" cy="8" r="3"/></g>
    <polyline points="26,76 46,58 70,60 92,48 114,50 136,60 160,44 182,36" fill="none" stroke="var(--orange)" stroke-width="1.2"/>
    <g fill="#fff" stroke="var(--orange)" stroke-width="1"><circle cx="26" cy="76" r="3"/><circle cx="46" cy="58" r="3"/><circle cx="70" cy="60" r="3"/><circle cx="92" cy="48" r="3"/><circle cx="114" cy="50" r="3"/><circle cx="136" cy="60" r="3"/><circle cx="160" cy="44" r="3"/><circle cx="182" cy="36" r="3"/></g>
  </svg>
  <svg width="180" height="82" viewBox="0 0 180 82" style="position:absolute;left:210px;top:68px" font-family="Roboto, Arial, sans-serif">
    <g font-size="5" fill="#333" text-anchor="end"><text x="10" y="8">80</text><text x="10" y="24">60</text><text x="10" y="40">40</text><text x="10" y="56">20</text><text x="10" y="72">0</text></g>
    <g stroke="#555" stroke-width=".5">
      <line x1="14" y1="6" x2="14" y2="70"/><line x1="32" y1="6" x2="32" y2="70"/><line x1="50" y1="6" x2="50" y2="70"/><line x1="68" y1="6" x2="68" y2="70"/><line x1="86" y1="6" x2="86" y2="70"/><line x1="104" y1="6" x2="104" y2="70"/><line x1="122" y1="6" x2="122" y2="70"/><line x1="140" y1="6" x2="140" y2="70"/><line x1="158" y1="6" x2="158" y2="70"/>
      <line x1="14" y1="70" x2="165" y2="70"/>
    </g>
    <polyline points="14,70 23,20 41,14 59,22 77,54 95,58 113,62 131,62 149,62" fill="none" stroke="var(--brown)" stroke-width="1.1"/>
    <g fill="var(--brown)"><circle cx="23" cy="20" r="2"/><circle cx="41" cy="14" r="2"/><circle cx="59" cy="22" r="2"/><circle cx="77" cy="54" r="2"/><circle cx="95" cy="58" r="2"/><circle cx="113" cy="62" r="2"/><circle cx="131" cy="62" r="2"/><circle cx="149" cy="62" r="2"/></g>
    <g font-size="4" fill="#444" text-anchor="middle"><text x="23" y="78">Lorem</text><text x="41" y="78">Lorem</text><text x="59" y="78">Lorem</text><text x="77" y="78">Lorem</text><text x="95" y="78">Lorem</text><text x="113" y="78">Lorem</text><text x="131" y="78">Lorem</text><text x="149" y="78">Lorem</text></g>
  </svg>
  <p class="chart-note" style="left:20px">Lorem Ipsum is simply dummy text of the printing and typesetting industry. Lorem Ipsum has been the industry's standard dummy text ever since the 1500s, when an unknown printer took a galley of type and scrambled.</p>
  <p class="chart-note" style="left:212px">Lorem Ipsum is simply dummy text of the printing and typesetting industry. Lorem Ipsum has been the industry's standard dummy text ever since the 1500s, when an unknown printer took a galley of type and scrambled.</p>
  <svg class="foot" width="406" height="10" viewBox="0 0 406 10"><rect x="0" y="5" width="38" height="5" fill="var(--brown)"/><text x="44" y="9" font-family="Roboto, Arial, sans-serif" font-size="7" fill="#333">1</text><polygon points="58,10 62,5 406,5 406,10" fill="var(--orange)"/></svg>
</section>

</body>
</html>
```